依頼詳細
デザインテイストのイメージは以下の通りです
・洗練された
・安心感のある
・落ち着いた
・信頼できる

「写真素材について」
事業所画像など一部提供可能ですが、基本的にはミルテフォトなどの素材もしくはイラストとの組み合わせでお願いいたします

「WFと原稿について」
レイアウトについてはある程度自由に変更していただいても結構です

「納品形態について」
psd xd aiなど劣化のないものであればなんでも大丈夫です

「選考のポイント」
デザイン性のみ
SEOやマーケティング的な提案は求めていません
元サイトURL一応載せておきますが形式的に作成したものですので
こちらと比較してのアドバイスなども求めていません
あくまでデザインで決めます

サイトURL
http://kurete-kaigo.net/
ページ数
5ページ
希望イメージ
シンプル 複雑
単色 カラフル
暗い 明るい
日常 高級
遊び心 厳粛
未来的 伝統的
女性的 男性的
希望する色
青系、水色系
納品ファイル
• 高解像度JPG (.jpg)
• イラストレーター形式 (.ai)
• フォトショップ形式 (.psd)
• PNG形式 (.png)
補足説明
提案の数が少ないので期限を延長いたします
■ 選んだ理由

限定された条件のなかで素晴らしいデザインをご提案いただきありがとうございました

■ 提案者全員のお礼・コメント

素材画像がない状態でのデザイン制作は難しかったと思います
その中で素晴らしい提案をいただきまして本当にありがとうございました

```html
<!DOCTYPE html>
<html lang="ja">
<head>
<meta charset="utf-8">
<title>訪問介護そよかぜ</title>
<link href="https://fonts.googleapis.com/css2?family=Noto+Sans+JP:wght@400;500;700&display=swap" rel="stylesheet">
<style>
:root{
  --blue:#2a9fd8;
  --blue-dark:#1b7fb8;
  --blue-light:#e5f2fa;
  --blue-pale:#f2f8fc;
  --navy:#24445c;
  --text:#333a40;
  --muted:#6b7680;
  --white:#ffffff;
  --line:#d7e6f0;
  --accent:#e0505a;
}
*{box-sizing:border-box;margin:0;padding:0}
html,body{width:1200px;height:4060px;overflow:hidden}
body{font-family:"Noto Sans JP",sans-serif;color:var(--text);background:var(--white);position:relative}
.abs{position:absolute}
.photo{position:absolute}
.btn{position:absolute;display:flex;align-items:center;justify-content:center;background:var(--blue);color:var(--white);font-weight:700;font-size:18px;border-radius:6px}
.section-title{position:absolute;left:0;width:1200px;text-align:center;font-size:34px;font-weight:700;color:var(--navy);letter-spacing:.08em}
.section-title::after{content:"";display:block;width:60px;height:3px;background:var(--blue);margin:14px auto 0}
p.small{font-size:14px;line-height:1.9;color:var(--text)}

/* header */
.header{position:absolute;top:0;left:0;width:1200px;height:96px;background:var(--white);z-index:5}
.logo{position:absolute;left:40px;top:24px;display:flex;align-items:center;gap:10px;font-size:20px;font-weight:700;color:var(--blue)}
.logo i{width:36px;height:36px;border-radius:50%;background:var(--blue);display:block}
.header .tel{position:absolute;left:690px;top:10px;font-size:22px;font-weight:700;color:var(--blue)}
.header .tel small{display:block;font-size:11px;color:var(--muted);font-weight:400}
.header .mail{position:absolute;left:930px;top:10px;width:210px;height:36px;border-radius:18px;background:var(--blue);color:#fff;font-size:14px;font-weight:700;display:flex;align-items:center;justify-content:center}
.gnav{position:absolute;left:440px;top:62px;display:flex;gap:44px;font-size:14px;color:var(--text)}

/* hero */
.hero-photo{left:0;top:0;width:1200px;height:820px;background:linear-gradient(120deg,#f4efe8 0%,#e9eef2 45%,#dfe9f1 100%)}
.hero-badge{left:1005px;top:360px;width:150px;height:150px;border-radius:50%;background:var(--blue);color:#fff;display:flex;flex-direction:column;align-items:center;justify-content:center;font-weight:700;font-size:26px;line-height:1.3}
.hero-badge b{font-size:38px}
.hero-copy{left:430px;top:600px;width:760px;height:140px;background:rgba(255,255,255,.92);padding:22px 40px;font-size:40px;font-weight:700;color:var(--navy);line-height:1.45}
.hero-copy em{font-style:normal;color:var(--blue);font-size:48px}

/* features */
.features{left:0;top:820px;width:1200px;height:900px;background:var(--blue-light)}
.feat-circle{position:absolute;z-index:3;border-radius:50%;background:var(--white);border:3px solid var(--blue);display:flex;align-items:center;justify-content:center;text-align:center;font-weight:700;color:var(--navy);font-size:17px;line-height:1.45}
.feat-circle span{color:var(--blue)}
.feat-box{position:absolute;z-index:2;background:var(--white);padding:22px 26px;box-shadow:0 4px 14px rgba(30,80,120,.08)}

/* services */
.card{position:absolute;top:1820px;width:510px;height:600px;background:var(--blue-pale)}
.card .pic{position:absolute;left:0;top:0;width:510px;height:300px}
.card .label{position:absolute;left:115px;top:280px;width:280px;height:56px;background:var(--white);border:2px solid var(--blue);color:var(--blue);font-weight:700;font-size:22px;display:flex;align-items:center;justify-content:center}
.card p{position:absolute;left:40px;top:360px;width:430px}
.card .btn{left:135px;top:500px;width:240px;height:54px}

/* usage */
.usage-photo{left:0;top:2490px;width:1200px;height:520px;background:linear-gradient(110deg,#a9bccb 0%,#c9d6df 45%,#dfe8ef 100%)}
.usage-title{left:440px;top:2510px;font-size:34px;font-weight:700;color:#fff;letter-spacing:.1em;text-shadow:0 2px 10px rgba(20,60,95,.55)}
.usage-card{left:600px;top:2580px;width:520px;height:230px;background:rgba(255,255,255,.95);padding:26px 30px 0 110px}
.usage-card h3{font-size:20px;color:var(--navy);line-height:1.5}
.usage-card h3 span{color:var(--accent)}
.usage-step{left:540px;top:2610px;width:110px;height:110px;border-radius:50%;background:var(--blue);color:#fff;font-weight:700;font-size:20px;display:flex;align-items:center;justify-content:center;text-align:center;line-height:1.3}

/* contact */
.contact{left:200px;top:2910px;width:820px;height:180px;background:var(--white);box-shadow:0 6px 20px rgba(30,80,120,.15)}
.free-badge{left:140px;top:2860px;width:120px;height:120px;border-radius:50%;background:var(--blue);color:#fff;font-weight:700;font-size:19px;display:flex;align-items:center;justify-content:center;text-align:center;line-height:1.3;transform:rotate(-12deg)}

/* news */
.news-side{left:150px;top:3160px;width:170px;height:240px;background:var(--blue-light)}
.news-list{left:380px;top:3170px;width:680px}
.news-item{display:flex;gap:40px;padding:22px 10px;border-bottom:1px solid var(--line);font-size:17px}
.news-item time{color:var(--muted);width:80px}

/* recruit */
.recruit{left:0;top:3440px;width:1200px;height:500px;background:linear-gradient(180deg,#f4f9fc,#e6f2f9)}
.recruit-photo{left:0;top:3440px;width:560px;height:500px;background:linear-gradient(160deg,#f6e9ea 0%,#e9f1f7 100%)}
.pill{position:absolute;background:var(--blue);color:#fff;font-weight:700;display:flex;align-items:center;justify-content:center}
.footer{left:0;top:3960px;width:1200px;height:100px;background:var(--white);border-top:1px solid var(--line)}
</style>
</head>
<body>

<div class="photo hero-photo" role="img" aria-label="在宅で介護スタッフが高齢の男性と笑顔で話している写真"></div>

<header class="header">
  <div class="logo"><i></i>訪問介護そよかぜ</div>
  <div class="tel">☎ 012-345-6789<small>受付 9:00〜18:00</small></div>
  <div class="mail">✉ メールで問い合わせ</div>
  <nav class="gnav"><span>特徴</span><span>ご利用について</span><span>提供サービス</span><span>事業所一覧</span><span>採用情報</span><span>運営会社</span></nav>
</header>

<div class="abs hero-badge">24時間<b>365日</b></div>
<div class="abs hero-copy">住み慣れたご自宅で<br><em>“自分らしい”</em>介護サービスを</div>

<section class="abs features">
  <svg class="abs" style="left:0;top:520px" width="1200" height="380" viewBox="0 0 1200 380"><path d="M0 200 C300 80 700 320 1200 160 L1200 380 L0 380Z" fill="#d3e9f6"/><path d="M0 270 C350 170 750 360 1200 250" stroke="#fff" stroke-width="3" fill="none" opacity=".8"/></svg>
</section>
<div class="section-title" style="top:870px">訪問介護そよかぜの特徴</div>

<div class="photo" style="left:450px;top:990px;width:380px;height:300px;background:linear-gradient(135deg,#cfe4f2,#eef5fa)" role="img" aria-label="介護スタッフが利用者の手を握る写真"></div>
<div class="feat-circle" style="left:380px;top:1100px;width:130px;height:130px"><div><span>24時間</span><br>365日対応</div></div>
<div class="feat-box" style="left:830px;top:990px;width:300px;height:230px"><p class="small">日中だけでなく夜間・早朝も訪問に伺います。急な体調の変化にも落ち着いて対応し、ご家族の負担を減らせるよう、いつでも相談できる体制を整えています。</p></div>
<div class="feat-circle" style="left:245px;top:1295px;width:160px;height:160px"><div>1人ひとりに<br>最適な<span>個別支援</span></div></div>
<div class="feat-box" style="left:70px;top:1420px;width:340px;height:170px"><p class="small">ケアマネジャーと連携し、ご本人の暮らし方や想いに合わせた支援計画を作成します。小さな変化も記録し、より良いケアにつなげます。</p></div>
<div class="feat-circle" style="left:695px;top:1300px;width:160px;height:160px"><div>医療機関と<br>連携して<br><span>安心・安全</span></div></div>
<div class="feat-box" style="left:790px;top:1420px;width:340px;height:170px"><p class="small">地域の医療機関や訪問看護と情報を共有し、健康状態に合わせたサービスを提供します。ご家族との連絡も丁寧に行います。</p></div>
<div class="btn" style="left:460px;top:1615px;width:280px;height:58px">特徴を詳しく見る</div>

<div class="section-title" style="top:1730px">提供サービス</div>
<div class="card" style="left:75px">
  <div class="photo pic" style="background:linear-gradient(140deg,#e8dccd,#f3ede4)" role="img" aria-label="スタッフが高齢の男性の立ち上がりを介助する写真"></div>
  <div class="label">訪問介護</div>
  <p class="small">介護職員がご自宅を訪問し、食事・入浴・排せつなどの身体介護や、掃除・洗濯・調理などの生活援助を行います。</p>
  <div class="btn">詳しく見る</div>
</div>
<div class="card" style="left:615px">
  <div class="photo pic" style="background:linear-gradient(140deg,#f1e2dc,#eaf1f5)" role="img" aria-label="スタッフが高齢の女性に食事を運ぶ写真"></div>
  <div class="label">居宅介護支援</div>
  <p class="small">ケアマネジャーがご相談を受け、心身の状態やご希望に合わせてケアプランを作成し、サービス事業者との調整を行います。</p>
  <div class="btn">詳しく見る</div>
</div>

<div class="photo usage-photo" role="img" aria-label="車椅子に座る利用者をスタッフが支える写真"></div>
<div class="abs usage-title">ご利用について</div>
<div class="abs usage-card">
  <h3>訪問介護のご利用には<span>要介護認定</span>が必要です</h3>
  <p class="small" style="margin-top:14px">まずはお住まいの市区町村の窓口で申請を行います。認定後、ケアマネジャーと相談しながらサービス内容を決めていきます。</p>
</div>
<div class="abs usage-step">手続き<br>の流れ</div>
<div class="btn" style="left:700px;top:2830px;width:300px;height:54px">利用の流れを詳しく見る</div>

<div class="abs contact">
  <div class="abs" style="left:0;top:24px;width:820px;text-align:center;font-size:22px;font-weight:700;color:var(--navy)">お気軽にお問い合わせください</div>
  <svg class="abs" style="left:110px;top:84px" width="46" height="60" viewBox="0 0 46 60"><rect x="4" y="2" width="38" height="56" rx="6" fill="var(--blue)"/><rect x="10" y="10" width="26" height="36" fill="#fff"/></svg>
  <div class="abs" style="left:170px;top:80px;font-size:30px;font-weight:700;color:var(--blue)">012-345-6789</div>
  <div class="abs" style="left:172px;top:124px;font-size:14px;color:var(--muted)">受付 9:00〜18:00</div>
  <div class="abs" style="left:500px;top:82px;width:260px;height:60px;border-radius:6px;background:var(--blue);color:#fff;font-weight:700;font-size:17px;display:flex;align-items:center;justify-content:center;gap:12px">
    <svg width="30" height="22" viewBox="0 0 30 22"><rect x="1" y="1" width="28" height="20" fill="none" stroke="#fff" stroke-width="2"/><path d="M1 1 L15 12 L29 1" fill="none" stroke="#fff" stroke-width="2"/></svg>メールで問い合わせ</div>
</div>
<div class="abs free-badge">無料相談<br>受付中</div>

<div class="abs news-side">
  <div class="abs" style="left:0;top:40px;width:170px;text-align:center;font-size:20px;font-weight:700;color:var(--navy)">お知らせ</div>
  <div class="abs" style="left:20px;top:160px;width:130px;height:44px;border-radius:4px;background:var(--blue);color:#fff;font-size:15px;font-weight:700;display:flex;align-items:center;justify-content:center">一覧を見る</div>
</div>
<div class="abs news-list">
  <div class="news-item"><time>○月○日</time><span>新事業所オープン</span></div>
  <div class="news-item"><time>○月○日</time><span>サービス管理責任者募集します</span></div>
  <div class="news-item"><time>○月○日</time><span>登録ヘルパー募集します</span></div>
</div>

<div class="abs recruit"></div>
<div class="photo recruit-photo" role="img" aria-label="笑顔の女性介護スタッフの写真"></div>
<div class="abs" style="left:620px;top:3470px;width:520px;text-align:center;font-size:20px;line-height:1.7;color:var(--navy);font-weight:500">「介護はそよかぜにお願いしたい」<br>地域の皆様の声にお応えするために！</div>
<div class="pill" style="left:650px;top:3555px;width:460px;height:54px;font-size:28px;border-radius:4px">スタッフ積極採用中</div>
<div class="abs" style="left:620px;top:3625px;width:520px;text-align:center;font-size:20px;font-weight:700;color:var(--navy);line-height:1.5">車両費・ガソリン代<br><span style="color:var(--blue)">全額会社負担</span></div>
<div class="abs" style="left:620px;top:3700px;width:520px;text-align:center;font-size:13px;color:var(--muted)">ガソリン代・車両代・メンテナンス費・保険代まで会社が負担します</div>
<div class="abs" style="left:600px;top:3740px;width:260px;text-align:center"><b style="font-size:17px;color:var(--navy)">1日1時間〜</b><br><b style="font-size:17px;color:var(--blue)">自由な働き方</b><b style="font-size:17px;color:var(--navy)">を応援</b><p class="small" style="margin-top:8px">週1日・短時間からOK。家庭やご自分の予定に合わせて無理なく働けます。</p></div>
<div class="abs" style="left:880px;top:3740px;width:270px;text-align:center"><b style="font-size:17px;color:var(--navy)">夜間・深夜</b><b style="font-size:17px;color:var(--blue)">時給1,875円</b><br><b style="font-size:17px;color:var(--navy)">有給取得率100%</b><p class="small" style="margin-top:8px">資格取得支援や研修制度も充実。経験を活かしてステップアップできます。</p></div>
<div class="btn" style="left:760px;top:3875px;width:240px;height:50px;border-radius:4px">採用情報</div>

<footer class="abs footer">
  <nav class="abs" style="left:120px;top:38px;display:flex;gap:70px;font-size:15px;color:var(--text)"><span>特徴</span><span>ご利用について</span><span>提供サービス</span><span>事業所一覧</span><span>採用情報</span><span>運営会社</span></nav>
</footer>

</body>
</html>
```